We are a building company that build new homes and units we are looking for something fresh and looks good my company name is
Larkmoor Building Group Pty Ltd

Industry/Entity Type

Building

Contact Information for Business Card

Name Marco Delacruz-Fenn
Tittle: Director
Address 14 Quarrel St. Thornbury Vic 3071
Ph: 03 9612 4087
Mobile : 0400 562 938

www.larkmoorbuildinggroup.com.au
Email: sales@larkmoorbuildinggroup.com.au

```html
<!DOCTYPE html>
<html lang="en">
<head>
<meta charset="utf-8">
<title>Larkmoor Building Group – Business Card</title>
<link rel="stylesheet" href="https://fonts.googleapis.com/css2?family=Michroma&family=Abel&family=Kalam&family=Arimo&display=swap">
<style>
  :root {
    --page: #ffffff;
    --grey-light: #6c6d70;
    --grey-mid: #535457;
    --grey-dark: #38393b;
    --brand-blue: #25a9e2;
    --card-blue: #00b4ee;
    --card-blue-deep: #0098d4;
    --curve-edge: #163a52;
    --white: #ffffff;
    --ink: #17191b;
  }
  html, body {
    margin: 0;
    padding: 0;
    width: 993px;
    height: 1200px;
    overflow: hidden;
    background: var(--page);
  }
  .canvas {
    position: relative;
    width: 993px;
    height: 1200px;
  }
  .card {
    position: absolute;
    left: 55px;
    width: 881px;
    overflow: hidden;
    box-shadow: 0 3px 8px rgba(0,0,0,0.35);
  }
  .card--front { top: 47px; height: 542px; }
  .card--back  { top: 610px; height: 546px; }
  .card__bg {
    position: absolute;
    inset: 0;
    width: 100%;
    height: 100%;
  }
  .brand {
    position: absolute;
    font-family: "Michroma", sans-serif;
    color: var(--brand-blue);
    letter-spacing: 3px;
    line-height: 1;
    margin: 0;
    font-weight: 400;
  }
  .brand__line { display: block; }
  .brand-square {
    position: absolute;
    background: var(--brand-blue);
  }
  .card--front .brand-square { left: 330px; top: 292px; width: 64px; height: 64px; }
  .card--front .brand { left: 414px; top: 294px; font-size: 23px; }
  .card--front .brand__line + .brand__line { margin-top: 14px; }
  .rule {
    position: absolute;
    left: 332px;
    top: 397px;
    width: 549px;
    height: 2px;
    background: var(--white);
  }
  .tagline {
    position: absolute;
    font-family: "Kalam", cursive;
    color: var(--white);
    margin: 0;
    line-height: 1;
  }
  .card--front .tagline { left: 419px; top: 420px; font-size: 25px; }

  .divider {
    position: absolute;
    left: 415px;
    top: 43px;
    width: 2px;
    height: 160px;
    background: var(--white);
  }
  .card--back .brand { left: 451px; top: 66px; font-size: 21px; }
  .card--back .brand__line + .brand__line { margin-top: 14px; }
  .card--back .tagline { left: 451px; top: 154px; font-size: 21px; }

  .contact {
    position: absolute;
    left: 95px;
    top: 270px;
    color: var(--ink);
    margin: 0;
  }
  .contact__name {
    font-family: "Abel", sans-serif;
    font-size: 35px;
    margin: 0 0 14px;
    font-weight: 400;
    line-height: 1;
  }
  .contact__phone {
    font-family: "Abel", sans-serif;
    font-size: 28px;
    margin: 0 0 10px;
    line-height: 1.1;
  }
  .contact__web {
    font-family: "Arimo", sans-serif;
    font-size: 23px;
    margin: 0 0 12px;
    line-height: 1.2;
  }
  .contact__phone:last-of-type { margin-bottom: 18px; }
</style>
</head>
<body>
<main class="canvas">

  <section class="card card--front" aria-label="Business card front">
    <svg class="card__bg" viewBox="0 0 881 542" preserveAspectRatio="none" aria-hidden="true">
      <defs>
        <linearGradient id="front-base" x1="0" y1="0" x2="0" y2="1">
          <stop offset="0" stop-color="#4a4b4e"/>
          <stop offset="1" stop-color="#343537"/>
        </linearGradient>
        <linearGradient id="front-arc" x1="0" y1="0" x2="0" y2="1">
          <stop offset="0" stop-color="#727376"/>
          <stop offset="1" stop-color="#4b4c4f"/>
        </linearGradient>
      </defs>
      <rect width="881" height="542" fill="url(#front-base)"/>
      <path d="M0 0 H881 V0 C760 120 520 300 0 335 Z" fill="url(#front-arc)"/>
      <path d="M0 335 C520 300 760 120 881 0" fill="none" stroke="#3a3b3d" stroke-width="3" opacity="0.6"/>
    </svg>
    <div class="brand-square" aria-hidden="true"></div>
    <h1 class="brand">
      <span class="brand__line">LARKMOOR BUILDING</span>
      <span class="brand__line">GROUP</span>
    </h1>
    <div class="rule" aria-hidden="true"></div>
    <p class="tagline">New home design and construction</p>
  </section>

  <section class="card card--back" aria-label="Business card back">
    <svg class="card__bg" viewBox="0 0 881 546" preserveAspectRatio="none" aria-hidden="true">
      <defs>
        <linearGradient id="back-grey" x1="0" y1="0" x2="1" y2="1">
          <stop offset="0" stop-color="#55565a"/>
          <stop offset="0.6" stop-color="#707174"/>
          <stop offset="1" stop-color="#5c5d60"/>
        </linearGradient>
        <linearGradient id="back-blue" x1="0" y1="0" x2="0" y2="1">
          <stop offset="0" stop-color="#00a6e3"/>
          <stop offset="1" stop-color="#00b7f0"/>
        </linearGradient>
      </defs>
      <rect width="881" height="546" fill="url(#back-grey)"/>
      <path d="M0 0 C150 110 330 200 500 255 C650 300 780 320 881 330 V546 H0 Z" fill="url(#back-blue)"/>
      <path d="M0 0 C150 110 330 200 500 255 C650 300 780 320 881 330" fill="none" stroke="var(--curve-edge)" stroke-width="6"/>
    </svg>
    <div class="divider" aria-hidden="true"></div>
    <h2 class="brand">
      <span class="brand__line">LARKMOOR BUILDING</span>
      <span class="brand__line">GROUP</span>
    </h2>
    <p class="tagline">Quality, excellence and innovation</p>
    <address class="contact">
      <p class="contact__name">Marco Delacruz-Fenn</p>
      <p class="contact__phone">Ph: 03 9612 4087</p>
      <p class="contact__phone">Mobile: 0400 562 938</p>
      <p class="contact__web">www.larkmoorbuildinggroup.com.au</p>
      <p class="contact__web">Email: sales@larkmoorbuildinggroup.com.au</p>
    </address>
  </section>

</main>
</body>
</html>
```